Business Card Design

We sell fish products to corporate food companies who then turn these products into final food products for consumers

Industry/Entity Type

Business

Contact Information for Business Card

I need a corporate business card template for a fish products business. We would like it be professional for use in dealing with multi national companies. This company business card template will be used by multiple employees so the following fields must be open to edit (Name, Phone Number and Email address)

```html
<!DOCTYPE html>
<html lang="en">
<head>
<meta charset="utf-8">
<title>Tidewater Seafoods – Business Card</title>
<link href="https://fonts.googleapis.com/css2?family=Open+Sans:wght@400;600&display=swap" rel="stylesheet">
<style>
  :root {
    --stage: #e9e6e1;
    --card: #fbfbfb;
    --card-shade: #ececec;
    --navy: #1c4f9f;
    --deep-blue: #0b48a4;
    --sky: #35bde3;
    --sky-light: #6fd0ec;
    --rule: #9a9a9a;
    --ink: #3a3a3a;
  }
  html, body {
    margin: 0;
    width: 1200px;
    height: 718px;
    overflow: hidden;
    background: var(--stage);
    font-family: "Open Sans", Arial, sans-serif;
  }
  .business-card {
    position: absolute;
    left: 130px;
    top: 89px;
    width: 940px;
    height: 540px;
    background: radial-gradient(ellipse at 35% 40%, var(--card) 40%, var(--card-shade) 100%);
    box-shadow: 0 14px 30px rgba(0,0,0,0.22);
    overflow: hidden;
  }
  .wave-art {
    position: absolute;
    inset: 0;
    width: 940px;
    height: 540px;
  }
  .brand {
    position: absolute;
    left: 62px;
    top: 150px;
    display: flex;
    align-items: center;
    gap: 14px;
    color: var(--navy);
    font-weight: 400;
  }
  .brand-dot {
    width: 46px;
    height: 46px;
    border-radius: 50%;
    background: var(--navy);
    flex: none;
  }
  .brand-name {
    font-size: 34px;
    line-height: 1.05;
    letter-spacing: 1px;
  }
  .divider {
    position: absolute;
    top: 252px;
    height: 1px;
    background: var(--rule);
  }
  .divider-left { left: 270px; width: 205px; }
  .divider-right { left: 700px; width: 150px; }
  .holder-name {
    position: absolute;
    left: 490px;
    top: 231px;
    margin: 0;
    font-size: 28px;
    line-height: 40px;
    font-weight: 400;
    color: var(--navy);
    white-space: nowrap;
  }
  .contact-list {
    position: absolute;
    left: 520px;
    top: 282px;
    margin: 0;
    padding: 0;
    list-style: none;
    font-size: 18px;
    color: var(--ink);
  }
  .contact-list li {
    display: flex;
    align-items: center;
    gap: 12px;
    height: 38px;
  }
  .contact-icon { width: 18px; height: 18px; flex: none; }
</style>
</head>
<body>
  <div class="business-card">
    <svg class="wave-art" viewBox="0 0 940 540" aria-hidden="true">
      <path d="M940 50 C900 90 900 200 860 290 C825 370 745 415 610 445 C760 425 860 385 900 305 C925 245 935 170 940 120 Z" fill="var(--deep-blue)"/>
      <path d="M940 150 C925 280 880 390 740 450 C600 490 470 490 410 540 L940 540 Z" fill="var(--sky)"/>
      <path d="M940 175 C925 300 885 410 750 468 C620 505 500 505 440 540 L940 540 Z" fill="var(--sky-light)"/>
    </svg>

    <div class="brand">
      <span class="brand-dot"></span>
      <span class="brand-name">TIDEWATER<br>SEAFOODS</span>
    </div>

    <span class="divider divider-left"></span>
    <h1 class="holder-name">Marek Dalton</h1>
    <span class="divider divider-right"></span>

    <ul class="contact-list">
      <li>
        <svg class="contact-icon" viewBox="0 0 20 20" aria-hidden="true">
          <path d="M5 2 L8 6 L6 8 C7 11 9 13 12 14 L14 12 L18 15 L16 18 C9 18 2 11 2 4 Z" fill="var(--sky)"/>
        </svg>
        <span class="contact-phone">555-014-2376</span>
      </li>
      <li>
        <svg class="contact-icon" viewBox="0 0 20 20" aria-hidden="true">
          <rect x="2" y="5" width="16" height="11" rx="1" fill="var(--sky)"/>
          <path d="M2 5 L10 11 L18 5" fill="none" stroke="#ffffff" stroke-width="1.5"/>
        </svg>
        <span class="contact-email">marek@tidewaterseafoods.com</span>
      </li>
    </ul>
  </div>
</body>
</html>
```